Poster Design Project

Simple, very easy design project.

Design for a 20" x 30" poster (I will print the poster, you do the high-res design), of the attached.

(Pls note, this JPG is sideways and is an error). You are designing PORTRAIT

```html
<!DOCTYPE html>
<html lang="en">
<head>
<meta charset="utf-8">
<title>Great Ecommerce</title>
<link rel="stylesheet" href="https://fonts.googleapis.com/css2?family=Open+Sans:wght@700;800&display=swap">
<style>
  :root {
    --teal: #1a8896;
    --teal-light: #2b9aa7;
    --ink: #0a0a0a;
    --text: #2b2b2b;
    --paper: #ffffff;
  }
  html, body {
    margin: 0;
    padding: 0;
    overflow: hidden;
  }
  .poster {
    position: relative;
    width: 800px;
    height: 1200px;
    background: var(--paper);
    overflow: hidden;
    font-family: "Open Sans", "Segoe UI", sans-serif;
  }
  .top-band {
    position: absolute;
    top: 0;
    left: 0;
    width: 800px;
    height: 44px;
    background: var(--teal);
  }
  .title {
    position: absolute;
    top: 88px;
    left: 0;
    width: 800px;
    margin: 0;
    text-align: center;
    font-weight: 800;
    letter-spacing: -1px;
  }
  .title-line {
    display: block;
  }
  .title-great {
    color: var(--ink);
    font-size: 90px;
    line-height: 88px;
  }
  .title-ecommerce {
    color: var(--teal);
    font-size: 96px;
    line-height: 88px;
  }
  .values {
    position: absolute;
    top: 370px;
    left: 0;
    margin: 0;
    padding: 0;
    list-style: none;
  }
  .value {
    position: absolute;
    left: 50px;
    display: flex;
    align-items: center;
    white-space: nowrap;
    color: var(--text);
    font-size: 38px;
    font-weight: 700;
    line-height: 48px;
  }
  .value-marker {
    width: 28px;
    height: 24px;
    margin-right: 56px;
    flex: none;
  }
  .value-marker polygon { fill: var(--teal); }
  .value:nth-child(1) { top: 0; }
  .value:nth-child(2) { top: 78px; }
  .value:nth-child(3) { top: 152px; }
  .value:nth-child(4) { top: 220px; }
  .value:nth-child(5) { top: 294px; }
  .value:nth-child(6) { top: 368px; }
  .bottom-band {
    position: absolute;
    top: 830px;
    left: 0;
    width: 800px;
    height: 370px;
    background: var(--teal);
  }
  .icon-cluster {
    position: absolute;
    top: 14px;
    left: 104px;
    width: 584px;
    height: 344px;
    border-radius: 40px;
    background: radial-gradient(ellipse at center, var(--teal-light) 0%, var(--teal) 75%);
  }
</style>
</head>
<body>
<div class="poster">
  <div class="top-band"></div>

  <h1 class="title">
    <span class="title-line title-great">Great</span>
    <span class="title-line title-ecommerce">Ecommerce</span>
  </h1>

  <ul class="values">
    <li class="value"><svg class="value-marker" viewBox="0 0 28 24"><polygon points="7,0 21,0 28,12 21,24 7,24 0,12"/></svg>Diversity of Thought</li>
    <li class="value"><svg class="value-marker" viewBox="0 0 28 24"><polygon points="7,0 21,0 28,12 21,24 7,24 0,12"/></svg>Desire to Learn</li>
    <li class="value"><svg class="value-marker" viewBox="0 0 28 24"><polygon points="7,0 21,0 28,12 21,24 7,24 0,12"/></svg>Never Settle</li>
    <li class="value"><svg class="value-marker" viewBox="0 0 28 24"><polygon points="7,0 21,0 28,12 21,24 7,24 0,12"/></svg>Be a Problem Solver</li>
    <li class="value"><svg class="value-marker" viewBox="0 0 28 24"><polygon points="7,0 21,0 28,12 21,24 7,24 0,12"/></svg>Work Fast (Web Speed)</li>
    <li class="value"><svg class="value-marker" viewBox="0 0 28 24"><polygon points="7,0 21,0 28,12 21,24 7,24 0,12"/></svg>Execution - A Way of Life</li>
  </ul>

  <div class="bottom-band">
    <div class="icon-cluster" role="img" aria-label="Cluster of white web and ecommerce icons: shopping cart, thumbs up, magnifiers, envelope, globe, calendar, chart, users, padlocks, RSS feed, home, gears and directional arrows"></div>
  </div>
</div>
</body>
</html>
```